Health & Fitness Author & Public Speaker Needs Visually Stunning Web Design!

We've FINALLY got around to launching a website for Belinda Marchetti - Australian Food Coach and Health & Fitness Expert. The website is to promote her new healthy eating program - "Bright Plate Living".
For a compehensive outline of exactly what we are after, please see the following attached files:
(1) Web Layout (wireframe, content/copy, links to photos to use, sample page we love)
(2) Style Guide (these are the colours, and overall feel we want)
Photos that we'd like used (of Belinda, and food/meals) can be found at these URL's:
Profile: https://www.filecrate.example/sh/q4r8vpl2m7xz/K3tPzWq9Lm
PicVault: https://www.filecrate.example/sh/b7nwe3ju1kd5/9hFrTy2Qxa
HINT:
Before you do ANYTHING - check out this site as it is pretty much EXACTLY what we're after, but with our branding/colours/style: http://tessamorrow.example/
As we will need to revamp our existing Chatterbook page & other printed material, there may be the potential for further work for the successful designer in the future.
Thanks & Good Luck!
Donovan Pryle
Marketing & Business Development Manager
Bright Plate Living
Women, Ages 24 - 45, Interested in Healthly Eating & Fitness
Business

```html
<!DOCTYPE html>
<html lang="en">
<head>
<meta charset="utf-8">
<title>Bright Plate Living</title>
<link href="https://fonts.googleapis.com/css2?family=Mulish:wght@400;600;700;800&family=Tinos&display=swap" rel="stylesheet">
<style>
:root{
  --pink:#e8175d;
  --purple:#9b0a8f;
  --ink:#333333;
  --dark:#3a3a3a;
  --text:#444444;
  --grey:#c4c3c4;
  --white:#ffffff;
  --field:#ffffff;
  --sans:'Mulish', Arial, sans-serif;
  --serif:'Tinos', 'Times New Roman', serif;
}
*{box-sizing:border-box;margin:0;padding:0}
html,body{width:794px;height:1200px;overflow:hidden;background:var(--white)}
body{position:relative;font-family:var(--sans);color:var(--text)}
.abs{position:absolute}

/* hero */
.hero{left:0;top:0;width:794px;height:428px;background:linear-gradient(180deg,#4d6a33 0%,#6f8f3c 45%,#8aa54a 75%,#7b8a45 100%)}
.hero-photo{left:0;top:0;width:794px;height:428px;background:radial-gradient(ellipse 200px 240px at 500px 230px,rgba(70,60,60,.55),rgba(70,60,60,0) 70%)}
.topbar{left:0;top:0;width:794px;height:44px;background:rgba(255,255,255,.85)}
.brand{left:37px;top:0;width:236px;height:118px;background:var(--white);border-radius:0 0 10px 10px;box-shadow:0 2px 6px rgba(0,0,0,.25);display:flex;align-items:center;justify-content:center;text-align:center;font-weight:800;font-size:26px;line-height:1.05;color:var(--purple)}
.nav{right:30px;top:9px;display:flex;align-items:center;font-weight:700;font-size:19px;color:var(--ink);white-space:nowrap}
.nav span.sep{color:var(--pink);margin:0 12px;font-weight:400}
.credit{left:578px;top:74px;width:185px;height:68px;background:rgba(255,255,255,.85);padding:8px 0 0 16px;font-size:9.5px;font-weight:600;color:var(--ink);line-height:1.35}
.credit .name{color:var(--pink);font-weight:800;font-size:13px;margin-bottom:2px}
.credit .mag{font-weight:800;font-size:11px}
.tag{left:37px;height:33px;padding:0 14px;line-height:33px;font-weight:800;font-size:22px;color:var(--white);white-space:nowrap}
.t-purple{background:var(--purple)}
.t-dark{background:var(--dark)}
.t-pink{background:var(--pink)}

/* signup band */
.band{left:0;top:428px;width:794px;height:55px;background:var(--pink);box-shadow:inset 0 3px 5px rgba(0,0,0,.2)}
.band-title{left:24px;top:434px;width:330px;text-align:center;color:var(--white);font-weight:800;font-size:14px;white-space:nowrap}
.band-sub{left:24px;top:454px;width:330px;text-align:center;color:var(--white);font-size:9.5px;line-height:1.3}
.field{height:25px;background:var(--field);border:1px solid #ccc;font-size:11px;color:#888;padding:5px 6px}
.btn{height:25px;background:linear-gradient(#f4f4f4,#d8d8d8);border:1px solid #aaa;border-radius:2px;font-size:10.5px;font-weight:700;color:var(--ink);text-align:center;line-height:23px;white-space:nowrap}

/* posts */
.post-title{left:37px;font-weight:700;font-size:23px;color:var(--ink);white-space:nowrap}
.post-date{left:37px;font-weight:800;font-size:13px;color:var(--pink)}
.post-img{left:37px;width:157px;height:114px;border:1px solid var(--pink)}
.post-body{left:204px;width:300px;font-size:12px;line-height:19.5px;color:var(--text)}
.more{left:204px;font-size:12.5px;color:var(--purple);display:flex;align-items:center;gap:5px}

/* sidebar */
.ad{left:520px;width:236px;border:1px solid #999}
.ad-bar{position:absolute;left:0;bottom:0;width:100%;height:27px;background:var(--dark);color:var(--white);font-size:18px;text-align:right;padding-right:10px;line-height:27px;display:flex;justify-content:flex-end;align-items:center;gap:7px}
.ad-label{position:absolute;right:4px;height:17px;padding:0 6px;font-size:11px;font-weight:800;color:var(--white);line-height:17px;white-space:nowrap}
.challenge-top{position:absolute;left:0;top:0;width:100%;height:30px;background:var(--pink);color:var(--white);font-family:var(--serif);font-size:20px;text-align:center;line-height:30px}
.challenge-copy{position:absolute;left:5px;top:60px;font-size:21px;line-height:25px;color:var(--purple)}
.challenge-copy .flat{color:var(--pink);font-size:18px}
.movement{left:520px;top:914px;width:236px;height:146px;background:var(--pink);border:1px solid #999}
.movement h3{position:absolute;left:0;top:6px;width:100%;text-align:center;font-size:19px;font-weight:800;color:var(--white)}
.movement p{position:absolute;left:8px;top:31px;width:220px;text-align:center;font-size:9px;font-weight:800;color:#fff6a8;line-height:1.25}

/* footer */
.footer{left:0;top:1104px;width:794px;height:96px;background:var(--grey)}
.foot-nav{left:37px;top:1124px;font-size:20px;color:var(--ink);white-space:nowrap}
.foot-nav .sep{color:var(--pink);margin:0 10px}
.copy{left:37px;top:1164px;font-size:9.5px;color:var(--ink)}
.social{top:1130px;width:44px;height:44px;background:var(--ink);color:var(--white);font-size:7px;font-weight:700;display:flex;align-items:center;justify-content:center;text-align:center}
</style>
</head>
<body>

<header>
  <div class="abs hero"></div>
  <div class="abs hero-photo" role="img" aria-label="Photo of Belinda sitting cross-legged on park grass with a water bottle, apple and boxing gloves"></div>
  <div class="abs topbar"></div>
  <div class="abs brand">Bright Plate<br>Living</div>
  <nav class="abs nav">
    <span>Home</span><span class="sep">|</span><span>About</span><span class="sep">|</span><span>The Plan</span><span class="sep">|</span><span>Shop</span>
  </nav>
  <div class="abs credit">
    <div class="name">Belinda Marchetti</div>
    Australian Food Coach and<br>Health &amp; Fitness Expert<br>As seen in <span class="mag">Vera Mode</span>
  </div>
  <div class="abs tag t-purple" style="top:231px">Get Slim</div>
  <div class="abs tag t-dark" style="top:269px">Boost Energy</div>
  <div class="abs tag t-pink" style="top:309px">Guilt Free</div>
  <div class="abs tag t-purple" style="top:348px">With Bright Plate Living</div>
</header>

<section class="signup">
  <div class="abs band"></div>
  <div class="abs band-title">Join the BRIGHT PLATE LIVING Movement!</div>
  <div class="abs band-sub">Get a weekly serving of Inspiration &amp; advice<br>that will change your life... Bring It On!</div>
  <div class="abs field" style="left:367px;top:442px;width:146px">First Name</div>
  <div class="abs field" style="left:526px;top:442px;width:145px">Email</div>
  <div class="abs btn" style="left:681px;top:442px;width:75px">Hook Me Up!</div>
</section>

<main>
  <article>
    <h2 class="abs post-title" style="top:498px">Lorem ipsum dolor sit amet</h2>
    <div class="abs post-date" style="top:527px">January 12, 2013</div>
    <div class="abs post-img" style="top:551px;background:linear-gradient(135deg,#e8e2d6,#cdb79a 55%,#b33a4a)" role="img" aria-label="Bowl of oats with raspberries and blueberries"></div>
    <p class="abs post-body" style="top:547px">Lorem ipsum dolor sit amet, consectetur adipiscing elit. Etiam leo nisi, fermentum a pulvinar vel, interdum vulputate odio. Nulla rutrum mattis suscipit. Fusce tincidunt elit ut nisl consequat in tristique turpis ali-quam.</p>
    <div class="abs more" style="top:646px">Read More <svg width="8" height="9" viewBox="0 0 8 9"><path d="M0 0L8 4.5L0 9Z" fill="#9b0a8f"/></svg></div>
  </article>
  <article>
    <h2 class="abs post-title" style="top:691px">Lorem ipsum dolor sit amet</h2>
    <div class="abs post-date" style="top:720px">January 1, 2013</div>
    <div class="abs post-img" style="top:744px;background:linear-gradient(135deg,#f2efe8,#8cb84a 50%,#d9c39a)" role="img" aria-label="Plate of fresh salad with a wrap"></div>
    <p class="abs post-body" style="top:740px">Lorem ipsum dolor sit amet, consectetur adipiscing elit. Etiam leo nisi, fermentum a pulvinar vel, interdum vulputate odio. Nulla rutrum mattis suscipit. Fusce tincidunt elit ut nisl consequat in tristique turpis ali-quam.</p>
    <div class="abs more" style="top:839px">Read More <svg width="8" height="9" viewBox="0 0 8 9"><path d="M0 0L8 4.5L0 9Z" fill="#9b0a8f"/></svg></div>
  </article>
  <article>
    <h2 class="abs post-title" style="top:884px">Lorem ipsum dolor sit amet</h2>
    <div class="abs post-date" style="top:913px">December 27, 2012</div>
    <div class="abs post-img" style="top:937px;background:linear-gradient(135deg,#f4f4f4,#dcdcdc)" role="img" aria-label="Printed meal plan sheet with a pen"></div>
    <p class="abs post-body" style="top:933px">Lorem ipsum dolor sit amet, consectetur adipiscing elit. Etiam leo nisi, fermentum a pulvinar vel, interdum vulputate odio. Nulla rutrum mattis suscipit. Fusce tincidunt elit ut nisl consequat in tristique turpis ali-quam.</p>
    <div class="abs more" style="top:1032px">Read More <svg width="8" height="9" viewBox="0 0 8 9"><path d="M0 0L8 4.5L0 9Z" fill="#9b0a8f"/></svg></div>
  </article>
</main>

<aside>
  <div class="abs ad" style="top:500px;height:193px;background:linear-gradient(90deg,#c9b9b0,#e6e0dc 50%,#f2eef0)">
    <div role="img" aria-label="Belinda holding fruit beside the guide book cover" style="position:absolute;inset:0 0 27px 0"></div>
    <div class="ad-label" style="top:110px;background:var(--purple)">The Ultimate</div>
    <div class="ad-label" style="top:129px;background:var(--dark)">BRIGHT PLATE LIVING Guide</div>
    <div class="ad-label" style="top:148px;background:var(--pink)">By Belinda Marchetti</div>
    <div class="ad-bar">Get Yours Now! <svg width="9" height="11" viewBox="0 0 9 11"><path d="M0 0L9 5.5L0 11Z" fill="#fff"/></svg></div>
  </div>

  <div class="abs ad" style="top:707px;height:193px;background:var(--white)">
    <div role="img" aria-label="Fit woman in workout top and shorts" style="position:absolute;right:0;top:30px;width:110px;height:136px;background:linear-gradient(180deg,#f7f0e8,#e6c8ac 60%,#f4f4f4)"></div>
    <div class="challenge-top">12 WEEK CHALLENGE</div>
    <div class="challenge-copy">HEALTHY<br>HAPPY &amp; HOT<br><span class="flat">In No Time Flat!</span></div>
    <div class="ad-bar">Join Us Now! <svg width="9" height="11" viewBox="0 0 9 11"><path d="M0 0L9 5.5L0 11Z" fill="#fff"/></svg></div>
  </div>

  <div class="abs movement">
    <h3>Join The Movement!</h3>
    <p>Join the Bright Plate Living Movement and get a free copy of the Kick Start Plan ($27.00 Value)!</p>
    <div role="img" aria-label="Guide book cover" style="position:absolute;left:18px;top:58px;width:64px;height:82px;background:linear-gradient(180deg,#ffffff,#f0d8e6 60%,#c0407e)"></div>
    <div class="field" style="position:absolute;left:97px;top:60px;width:132px;height:19px;padding:2px 6px">First Name</div>
    <div class="field" style="position:absolute;left:97px;top:85px;width:132px;height:19px;padding:2px 6px">Email</div>
    <div class="btn" style="position:absolute;left:97px;top:112px;width:132px;height:22px;line-height:20px">Sign Me Up!</div>
  </div>
</aside>

<footer>
  <div class="abs footer"></div>
  <nav class="abs foot-nav">Community<span class="sep">/</span>Free Resources<span class="sep">/</span>Press<span class="sep">/</span>Contact</nav>
  <div class="abs copy">Copyright © 2012 BRIGHT PLATE LIVING. All Rights Reserved.</div>
  <div class="abs social" style="left:608px">Chatter-<br>book</div>
  <div class="abs social" style="left:662px">Chirpline</div>
  <div class="abs social" style="left:716px">Stream-<br>Box</div>
</footer>

</body>
</html>
```